Electronic Music Artist needs an Album Cover

DRELL is an electronic musician from Boston, Massachusetts. He needs an album cover that captures the essence of his music. The album is called Lanterns, which represents his experiences growing up, positive and negative. He would like to see designs that involves color and creativity. Attached are some examples of artworks that DRELL likes. He also included a few of his original photos (optional to use. Using a photo will not effect his final decision!), and his logo.

Colors

Designer to choose colors to be used in the design.

Requirements
Must have
• My project must have the text "Lanterns" and "DRELL", and the logo (attached in the files). The logo should not be the main subject of the artwork. Everything must look aesthetically pleasing.
Nice to have
• It would be nice to have some sort of creative graphic design (see example album covers for reference). Also, in one of the references, there is a column on the left hand side with some text in it. That could be cool to include, but without the asian text.
Should not have
• The project should not have any other language besides English.

```html
<!DOCTYPE html>
<html lang="en">
<head>
<meta charset="utf-8">
<title>DRELL — Lanterns</title>
<link rel="stylesheet" href="https://fonts.googleapis.com/css2?family=Montserrat:wght@500;600&display=swap">
<style>
  :root {
    --page: #e6e6e6;
    --ink-black: #0d0b0c;
    --ink-white: #f4f2f2;
    --accent-red: #e3262b;
    --column-top: #d8552a;
    --column-mid: #a3263a;
    --column-low: #2a1a22;
    --sunset-a: #5a2a22;
    --sunset-b: #c88358;
    --stone-a: #7c7a76;
    --stone-b: #cfcdc8;
    --trees-a: #d9d9d9;
    --trees-b: #3a3a3a;
    --swirl-a: #3a1416;
    --swirl-b: #8b4a3a;
    --swirl-c: #2f3c6a;
  }
  * { margin: 0; padding: 0; box-sizing: border-box; }
  html, body { width: 845px; height: 1200px; overflow: hidden; }
  body { background: var(--page); position: relative; font-family: "Montserrat", sans-serif; }

  .album-cover {
    position: absolute; left: 0; top: 177px;
    width: 845px; height: 845px; overflow: hidden;
    background: linear-gradient(180deg, #3a1a1c 0%, #1a1416 45%, #232122 75%, var(--ink-black) 100%);
  }

  .name-column {
    position: absolute; left: 0; top: 0; width: 155px; height: 845px;
    background: linear-gradient(180deg, var(--column-top) 0%, #e26a36 20%, var(--column-mid) 55%, var(--column-low) 85%, #151012 100%);
  }
  .artist-mark {
    position: absolute; left: 30px; top: 26px; width: 95px;
    display: flex; align-items: center; gap: 10px;
    color: var(--ink-white); font-weight: 600; font-size: 20px; letter-spacing: 3px;
  }
  .artist-mark .mark-square { width: 14px; height: 14px; background: var(--ink-white); flex: none; }
  .artist-name {
    position: absolute; left: 78px; top: 810px;
    transform: rotate(-90deg); transform-origin: 0 0;
    translate: -62px 0;
    font-size: 126px; font-weight: 500; line-height: 1; letter-spacing: 8px;
    color: transparent; -webkit-text-stroke: 3px var(--ink-white);
    white-space: nowrap;
  }

  .photo { position: absolute; }
  .photo-sunset { left: 160px; top: 0; width: 470px; height: 120px;
    background: linear-gradient(100deg, var(--sunset-a), var(--sunset-b) 45%, #e8c7a2 60%, var(--sunset-a)); }
  .photo-bridge { left: 160px; top: 140px; width: 300px; height: 300px;
    background: linear-gradient(180deg, var(--stone-b) 0%, var(--stone-a) 55%, #3c3b39 100%); }
  .photo-trees { left: 600px; top: 60px; width: 245px; height: 340px;
    background: radial-gradient(circle at 70% 20%, #ffffff 0%, var(--trees-a) 25%, #777 60%, var(--trees-b) 100%); }
  .photo-swirl { left: 380px; top: 380px; width: 465px; height: 180px;
    background: linear-gradient(120deg, var(--swirl-c) 0%, var(--swirl-a) 30%, var(--swirl-b) 55%, #d9a87e 70%, var(--swirl-a) 100%); }
  .photo-haze { left: 160px; top: 560px; width: 685px; height: 285px;
    background: linear-gradient(180deg, rgba(60,58,60,0.7), rgba(13,11,12,0)); }

  .title-grid { position: absolute; inset: 0; }
  .glyph {
    position: absolute; width: 60px; text-align: center;
    font-size: 48px; font-weight: 500; line-height: 1;
    color: var(--ink-white); transform: translate(-50%, -50%);
  }
  .glyph.is-lit { color: var(--accent-red); font-weight: 600; }
  .glyph.is-blurred { filter: blur(3px); opacity: 0.75; transform: translate(-50%, -50%) scaleX(1.5); }
  .glyph.is-faded { opacity: 0.55; }
</style>
</head>
<body>
  <main class="album-cover">
    <div class="photo photo-sunset" role="img" aria-label="Collage strip of a warm sunset sky"></div>
    <div class="photo photo-bridge" role="img" aria-label="Photograph of an old stone arch bridge over a river"></div>
    <div class="photo photo-trees" role="img" aria-label="Photograph of trees against a bright sun"></div>
    <div class="photo photo-swirl" role="img" aria-label="Abstract liquid swirl of red, brown and blue"></div>
    <div class="photo photo-haze" role="img" aria-label="Soft grey blurred texture"></div>

    <aside class="name-column">
      <div class="artist-mark"><span class="mark-square"></span><span>DRELL</span></div>
      <h1 class="artist-name">DRELL</h1>
    </aside>

    <h2 class="title-grid" aria-label="Lanterns">
      <span class="glyph" style="left:378px;top:107px">L</span>
      <span class="glyph is-lit" style="left:524px;top:107px">L</span>
      <span class="glyph is-blurred" style="left:660px;top:107px">L</span>

      <span class="glyph is-lit" style="left:378px;top:194px">A</span>
      <span class="glyph" style="left:524px;top:194px">A</span>

      <span class="glyph is-faded" style="left:378px;top:281px">N</span>
      <span class="glyph is-lit" style="left:524px;top:281px">N</span>
      <span class="glyph is-faded" style="left:660px;top:281px">N</span>

      <span class="glyph is-lit" style="left:378px;top:359px">T</span>
      <span class="glyph" style="left:524px;top:359px">T</span>
      <span class="glyph is-faded" style="left:660px;top:359px">T</span>

      <span class="glyph is-lit" style="left:378px;top:440px">E</span>
      <span class="glyph" style="left:470px;top:440px">E</span>
      <span class="glyph" style="left:560px;top:440px">E</span>
      <span class="glyph" style="left:660px;top:440px">E</span>

      <span class="glyph is-lit" style="left:378px;top:520px">R</span>
      <span class="glyph" style="left:524px;top:520px">R</span>
      <span class="glyph" style="left:660px;top:520px">R</span>
      <span class="glyph" style="left:776px;top:520px">R</span>

      <span class="glyph" style="left:378px;top:601px">N</span>
      <span class="glyph is-lit" style="left:524px;top:601px">N</span>
      <span class="glyph" style="left:660px;top:601px">N</span>
      <span class="glyph is-blurred" style="left:776px;top:601px">N</span>

      <span class="glyph" style="left:378px;top:688px">S</span>
      <span class="glyph is-lit" style="left:524px;top:688px">S</span>
      <span class="glyph" style="left:660px;top:688px">S</span>
      <span class="glyph is-blurred" style="left:776px;top:688px">S</span>
    </h2>
  </main>
</body>
</html>
```